Business card design for Lovanka massages

Independant massage therapist. I am looking for a new card design that is attractive and modern. It is important that the logo is on the card and when you see it, you know that this person is a massage therapist.
I would also like to have the QR code that send you to the website (www.lovankamassages-demo.ch).
The following contact informations, I would also like to be mentionned :
Pierre-Olivier "Polo" Marchemont
Massothérapeute
079 513 08 42
lovan.ka@exemple-mail.ch
www.lovankamassages-demo.ch
Chemin des Vergers 7
1999 Valmorin
Therapist
logo, massage, contact details
Designer to choose colors to be used in the design.

```html
<!DOCTYPE html>
<html lang="fr">
<head>
<meta charset="utf-8">
<title>Lovanka massages – carte de visite</title>
<link rel="stylesheet" href="https://fonts.googleapis.com/css2?family=Montserrat:wght@800&family=Lato:wght@400;700&family=Arimo:wght@400&display=swap">
<style>
  :root {
    --backdrop: #1b1b1b;
    --kraft-light: #dfbd93;
    --kraft-mid: #c99f6e;
    --kraft-dark: #a6794c;
    --ink: #111111;
    --code-fill: #1d1a16;
  }
  * { margin: 0; padding: 0; box-sizing: border-box; }
  html, body {
    width: 1093px;
    height: 1200px;
    overflow: hidden;
    background: var(--backdrop);
  }
  .canvas {
    position: relative;
    width: 1093px;
    height: 1200px;
  }
  .card {
    position: absolute;
    left: 265px;
    width: 580px;
    height: 356px;
    background: linear-gradient(150deg, var(--kraft-light) 0%, var(--kraft-mid) 50%, var(--kraft-dark) 100%);
    color: var(--ink);
  }
  .card--contact { top: 226px; }
  .card--brand { top: 620px; }

  .contact {
    position: absolute;
    top: 70px;
    left: 0;
    width: 100%;
    text-align: center;
    font-family: "Lato", sans-serif;
  }
  .contact__name {
    font-family: "Montserrat", sans-serif;
    font-weight: 800;
    font-size: 19px;
    letter-spacing: 0.2px;
    line-height: 24px;
  }
  .contact__role {
    font-family: "Arimo", sans-serif;
    font-size: 16px;
    line-height: 18px;
  }
  .contact__rule {
    width: 94px;
    height: 1px;
    background: var(--ink);
    margin: 15px auto 14px;
  }
  .contact__details,
  .contact__address {
    list-style: none;
    font-size: 16.5px;
    line-height: 21px;
  }
  .contact__details + .contact__rule { margin: 8px auto 13px; }

  .qr-code {
    position: absolute;
    right: 26px;
    bottom: 26px;
    width: 64px;
    height: 64px;
    background: var(--code-fill);
  }

  .brand {
    position: absolute;
    top: 50%;
    left: 50%;
    transform: translate(-50%, -50%);
    display: flex;
    align-items: center;
    gap: 14px;
  }
  .brand__dot {
    width: 30px;
    height: 30px;
    border-radius: 50%;
    background: var(--ink);
  }
  .brand__name {
    font-family: "Lato", sans-serif;
    font-weight: 700;
    font-size: 62px;
    line-height: 1;
    color: var(--ink);
  }
</style>
</head>
<body>
<main class="canvas">
  <section class="card card--contact">
    <div class="contact">
      <h1 class="contact__name">PIERRE-OLIVIER “POLO” MARCHEMONT</h1>
      <p class="contact__role">Massothérapeute</p>
      <div class="contact__rule"></div>
      <ul class="contact__details">
        <li>M: 079 513 08 42</li>
        <li>E: lovan.ka@exemple-mail.ch</li>
        <li>W: www.lovankamassages-demo.ch</li>
      </ul>
      <div class="contact__rule"></div>
      <ul class="contact__address">
        <li>Chemin des Vergers 7</li>
        <li>1999 Valmorin</li>
      </ul>
    </div>
    <div class="qr-code" role="img" aria-label="QR code vers www.lovankamassages-demo.ch"></div>
  </section>

  <section class="card card--brand">
    <div class="brand">
      <span class="brand__dot"></span>
      <span class="brand__name">Lovanka</span>
    </div>
  </section>
</main>
</body>
</html>
```